Book Cover for a book on Lantern Road Ventures

I am self-publishing my book on Brindlemark and need a book cover made. Below are the details. See attached templates for size we need to use. I also attached a previous cover we had made that I liked. The problem with it was they were two boys helping each other but the book is about women. I'm open to your ideas on the cover though, but I wanted to show you a style I liked as an idea.
Front of Cover
Book Title: Lantern Road Ventures
Book Subtitle: Loose Pages of a Harbor Keeper
Author Name: Mirela T. Dunbar
Add on the Spine of Cover: Lantern Road Ventures and Mirela T. Dunbar
Back of the Cover Text:
Lantern Road Ventures: Loose Pages of a Harbor Keeper is an honest account of a business owner’s experience attempting to navigate the start-up community while also pursuing spiritual growth. Author Mirela Dunbar defines a spiritual entrepreneur as “someone who runs an enterprise with the purpose of growing love rather than material gain.” This book discusses the three dimensions of Lantern Road Ventures:
1. The business is an integral part of the founder’s spiritual journey.
2. Employees working for the spiritual enterprise, whether they know it or not, encounter this company because it's part of their spiritual path.
3. The business itself has a life force of its own and its purpose is to further the kingdom of heaven on earth.
These three dimensions happen simultaneously and work together to produce the greatest possible result. However, this can feel confusing to a founder juggling these dimensions while also trying to manage and run a business. This is not a formulaic self-help book or roadmap. Rather, it is a compilation of personal reflections that often seem at odds with the traditional world of entrepreneurship.
Below the description add my picture (see attached for my picture)
Bio text:
Mirela Dunbar founded Calveta with the vision of ushering in a life-long education system that shifts away from standardization to one that empowers people to live their purpose. In college, Mirela interned for Open Kettle, a women’s empowerment initiative where she recognized her passion for helping people find their voice. Mirela's 20-year journey has come full circle to empowering other female CEOs who are pursuing the path of Lantern Road Ventures.
NOTE: Please note that Brindlemark puts a bar code on the bottom right of the back cover as is noted on the attached template.
Size template is attached to the brief, here are the sizes typed out:
# Description Width (in) Height (in)
1 Full Cover 12.79 9.25
2 Front Cover 6 9
3 Safe Area 5.875 8.75
4 Bleed 0.125 0.125
5 Margin 0.125 0.125
6 Spine 0.54 9
7 Spine Safe Area 0.415 8.75
8 Spine Margin 0.062 0.062
9 Barcode Margin 0.25 0.25
Pre-publication checklist
BRINDLEMARK TIPS for the final cover:
1. Save as a PDF. Your cover must be a single PDF that includes the back cover, spine, and front cover as one image.
2. Flatten all transparencies. These can cause the file to print with missing or distorted content. Consult your software's documentation to learn how.
3. Embed your fonts. Consult your software's documentation to learn how.
4. Remove crop marks, color bars, template text. Crop marks are lines showing where pages should be trimmed. Color bars are strips with a series of patches used to ensure color balance during printing. Also, remove any template text, PDF creation guides, or software references.
5. Ensure your cover image meets the minimum resolution of 300 DPI (dots per inch).
6. Optimize PDFs. Optimization is useful to reduce your file size, allowing for higher performance when transferring, uploading, viewing, and printing the files.
7. Remove file security. Locked or encrypted files will fail review.
Target Market(s)
Women who want to be CEOs or are currently CEOs of companies.
Industry/Entity Type
Entrepreneurship, business, spirituality
Requirements
Must have
- Just the text on the description. A very welcoming feel.
Nice to have
- I like the idea of having a sunrise/sunset in the image somehow like in the example I attached to the brief, but again I'm open.
Should not have
- Please don't put any yoga or meditation poses or hands outstretched. I have a lot of interesting ones that look like my example so if you are going to submit after Saturday 10/29, please only do so if you have a new idea! Thanks!

```html
<!DOCTYPE html>
<html lang="en">
<head>
<meta charset="utf-8">
<title>Lantern Road Ventures — Cover Spread</title>
<link rel="stylesheet" href="https://fonts.googleapis.com/css2?family=Alegreya:wght@400;700&family=Libre+Baskerville:wght@400&display=swap">
<style>
  :root {
    --ink: #000000;
    --spine: #151515;
    --paper: #ffffff;
    --ember: #e5762e;
    --ember-deep: #c95a1f;
    --sky-top: #a8431d;
    --sky-mid: #e0742d;
    --sky-glow: #f3a24a;
    --horizon: #1a0d08;
  }
  html, body {
    margin: 0;
    padding: 0;
    width: 1200px;
    height: 868px;
    overflow: hidden;
    background: var(--ink);
  }
  .spread {
    position: relative;
    width: 1200px;
    height: 868px;
    background: var(--ink);
    color: var(--paper);
    font-family: "Alegreya", Georgia, serif;
  }

  /* Back cover */
  .back-cover {
    position: absolute;
    left: 0; top: 0;
    width: 573px; height: 868px;
  }
  .blurb {
    position: absolute;
    left: 30px; top: 14px;
    width: 517px;
    font-size: 14px;
    line-height: 17.6px;
    text-align: justify;
    margin: 0;
  }
  .blurb p { margin: 0 0 17px; }
  .blurb-title { color: var(--ember); font-weight: 700; font-size: 17px; }
  .blurb-subtitle { font-weight: 700; }
  .dimensions {
    margin: 0 0 18px;
    padding-left: 28px;
    text-align: left;
  }
  .dimensions li { margin-bottom: 2px; }
  .author-portrait {
    position: absolute;
    left: 42px; top: 447px;
    width: 95px; height: 91px;
    background: linear-gradient(160deg, #9fae7c 0%, #6f8a57 45%, #c6485a 100%);
  }
  .bio {
    position: absolute;
    left: 148px; top: 446px;
    width: 399px;
    margin: 0;
    font-size: 14px;
    line-height: 17.6px;
    text-align: justify;
  }

  /* Spine */
  .spine {
    position: absolute;
    left: 573px; top: 0;
    width: 52px; height: 868px;
    background: var(--spine);
  }
  .spine-title, .spine-author {
    position: absolute;
    left: 50%;
    white-space: nowrap;
    transform-origin: center;
  }
  .spine-title {
    top: 245px;
    font-family: "Libre Baskerville", Georgia, serif;
    color: var(--ember);
    font-size: 17px;
    letter-spacing: 1.5px;
    transform: translate(-50%, -50%) rotate(90deg);
  }
  .spine-author {
    top: 720px;
    font-size: 19px;
    transform: translate(-50%, -50%) rotate(90deg);
  }

  /* Front cover */
  .front-cover {
    position: absolute;
    left: 625px; top: 0;
    width: 575px; height: 868px;
  }
  .front-scene {
    position: absolute;
    left: 0; top: 0;
    width: 575px; height: 392px;
    background:
      radial-gradient(ellipse 70% 45% at 55% 96%, var(--sky-glow) 0%, transparent 70%),
      linear-gradient(180deg, var(--sky-top) 0%, var(--sky-mid) 60%, var(--sky-glow) 88%, var(--horizon) 100%);
  }
  .front-title {
    position: absolute;
    left: 0; top: 452px;
    width: 575px;
    margin: 0;
    text-align: center;
    font-family: "Libre Baskerville", Georgia, serif;
    font-weight: 400;
    font-size: 43px;
    line-height: 59px;
    letter-spacing: 1px;
    color: var(--ember);
    background: linear-gradient(180deg, var(--ember) 0%, var(--ember-deep) 100%);
    -webkit-background-clip: text;
    background-clip: text;
    -webkit-text-fill-color: transparent;
  }
  .front-subtitle {
    position: absolute;
    left: 0; top: 612px;
    width: 575px;
    margin: 0;
    text-align: center;
    font-weight: 700;
    font-size: 21px;
  }
  .front-author {
    position: absolute;
    left: 0; top: 792px;
    width: 575px;
    margin: 0;
    text-align: center;
    font-size: 26px;
  }
</style>
</head>
<body>
<main class="spread">
  <section class="back-cover">
    <div class="blurb">
      <p><span class="blurb-title">Lantern Road Ventures:</span> <span class="blurb-subtitle">Loose Pages of a Harbor Keeper</span> is an honest account of a business owner’s experience attempting to navigate the start-up community while also pursuing spiritual growth. Author Mirela Dunbar defines a spiritual entrepreneur as “someone who runs an enterprise with the purpose of growing love rather than material gain.” This book discusses the three dimensions of Lantern Road Ventures:</p>
      <ul class="dimensions">
        <li>The business is an integral part of the founder’s spiritual journey.</li>
        <li>Employees working for the spiritual enterprise, whether they know it or not, encounter this company because it’s part of their spiritual path.</li>
        <li>The business itself has a life force of its own and its purpose is to further the kingdom of heaven on earth.</li>
      </ul>
      <p>These three dimensions happen simultaneously and work together to produce the greatest possible result. However, this can feel confusing to a founder juggling these dimensions while also trying to manage and run a business. This is not a formulaic self-help book or roadmap. Rather, it is a compilation of personal reflections that often seem at odds with the traditional world of entrepreneurship.</p>
    </div>
    <div class="author-portrait" role="img" aria-label="Portrait photograph of the author"></div>
    <p class="bio">Mirela Dunbar founded Calveta with the vision of ushering in a life-long education system that shifts away from standardization to one that empowers people to live their purpose. In college, Mirela interned for Open Kettle, a women’s empowerment initiative where she recognized her passion for helping people find their voice. Mirela’s 20-year journey has come full circle to empowering other female CEOs who are pursuing the path of Lantern Road Ventures.</p>
  </section>

  <section class="spine">
    <div class="spine-title">LANTERN ROAD VENTURES</div>
    <div class="spine-author">Mirela T. Dunbar</div>
  </section>

  <section class="front-cover">
    <div class="front-scene" role="img" aria-label="Photograph of three women in silhouette celebrating against an orange sunset sky"></div>
    <h1 class="front-title">LANTERN ROAD<br>VENTURES</h1>
    <p class="front-subtitle">Loose Pages of a Harbor Keeper</p>
    <p class="front-author">Mirela T. Dunbar</p>
  </section>
</main>
</body>
</html>
```